FenlyMedia - Biz Cards & Stationary
Need to print on Tuesday!
FenlyMedia - Biz Cards & Stationary -
Creative Brief
Professional
Tessa Crale
Principal
482 Marlow Lane Corbin Falls, Ohio 43990
tessa@fenlymedia-example.com
I will consider 2-sided biz cards if you have a cool idea. Also, if you think a different font will compliment the logo better, then suggest it. I will need two versions of the card in the end -- one with the title of "Principal" and the other with "Independent Account Director/Strategist". (Keep this in mind from a space standpoint.) Please also design letterhead and a #10 envelope. I'd also like to have a notecard (folds like a greeting card) and envelope for that.

```html
<!DOCTYPE html>
<html lang="en">
<head>
<meta charset="utf-8">
<title>FenlyMedia Business Card – Front and Back</title>
<link rel="stylesheet" href="https://fonts.googleapis.com/css2?family=Questrial&family=Montserrat:wght@700&display=swap">
<style>
  :root {
    --board-top: #14a39c;
    --board-mid: #1fa792;
    --board-bottom: #3db54a;
    --card: #ffffff;
    --teal: #1b9c96;
    --teal-soft: #3aa9a3;
    --green: #3db54a;
    --label: #e8f6f2;
    --shadow: rgba(0, 40, 30, 0.55);
  }
  * { margin: 0; padding: 0; box-sizing: border-box; }
  html, body { width: 1200px; height: 931px; overflow: hidden; }
  body {
    position: relative;
    background: linear-gradient(180deg, var(--board-top) 0%, var(--board-mid) 55%, var(--board-bottom) 100%);
    font-family: "Questrial", "Century Gothic", sans-serif;
  }
  .side-label {
    position: absolute;
    left: 284px;
    width: 630px;
    text-align: center;
    font-size: 17px;
    color: var(--label);
  }
  .side-label--front { top: 24px; }
  .side-label--back { top: 864px; }

  .card {
    position: absolute;
    left: 284px;
    width: 630px;
    height: 378px;
    background: var(--card);
    box-shadow: -14px 22px 22px var(--shadow);
    overflow: hidden;
  }
  .card--front { top: 52px; }
  .card--back { top: 477px; }
  .card-swoosh { position: absolute; inset: 0; width: 630px; height: 378px; }

  .card-name {
    position: absolute;
    left: 63px; top: 54px;
    font-size: 17px;
    color: var(--teal);
    letter-spacing: 0.5px;
  }
  .card-name strong {
    font-family: "Montserrat", "Century Gothic", sans-serif;
    font-weight: 700;
    font-size: 16px;
    margin-right: 12px;
  }
  .card-title { color: var(--teal-soft); }

  .brand-name {
    position: absolute;
    left: 60px; top: 184px;
    font-size: 66px;
    font-weight: 400;
    line-height: 1;
    color: var(--teal);
    letter-spacing: -1px;
  }

  .card-contact {
    position: absolute;
    left: 63px; top: 302px;
    font-size: 16px;
    font-style: normal;
    line-height: 25px;
    color: var(--teal);
  }
  .card-contact .divider {
    display: inline-block;
    width: 2px; height: 15px;
    margin: 0 8px;
    background: var(--green);
    vertical-align: -2px;
  }

  .card-web {
    position: absolute;
    left: 0; right: 0; top: 171px;
    text-align: center;
    font-size: 22px;
    color: var(--teal);
    letter-spacing: 0.3px;
  }
</style>
</head>
<body>
  <div class="side-label side-label--front">Bizcard Front</div>

  <section class="card card--front" aria-label="Business card front">
    <svg class="card-swoosh" viewBox="0 0 630 378" aria-hidden="true">
      <defs>
        <linearGradient id="swoosh-front" x1="0" y1="0" x2="1" y2="1">
          <stop offset="0" stop-color="#2faa4c"/>
          <stop offset="1" stop-color="#7cc84e"/>
        </linearGradient>
      </defs>
      <path d="M300 0 C450 0 600 50 630 205 L630 0 Z" fill="url(#swoosh-front)"/>
      <path d="M360 0 C490 10 590 65 622 190" fill="none" stroke="#a6dc80" stroke-width="1.5" opacity="0.7"/>
      <path d="M420 0 C520 18 600 75 626 170" fill="none" stroke="#b9e58f" stroke-width="1" opacity="0.6"/>
    </svg>

    <p class="card-name"><strong>TESSA CRALE</strong><span class="card-title">Principal</span></p>

    <h1 class="brand-name">FENLYMEDIA</h1>

    <address class="card-contact">
      <div>482 Marlow Lane<span class="divider"></span>Corbin Falls, Ohio 43990</div>
      <div>312-555-0148<span class="divider"></span>tessa@fenlymedia-example.com</div>
    </address>
  </section>

  <section class="card card--back" aria-label="Business card back">
    <svg class="card-swoosh" viewBox="0 0 630 378" aria-hidden="true">
      <defs>
        <linearGradient id="swoosh-back" x1="0" y1="0" x2="1" y2="1">
          <stop offset="0" stop-color="#2faa4c"/>
          <stop offset="1" stop-color="#7cc84e"/>
        </linearGradient>
      </defs>
      <path d="M450 0 C560 8 615 55 630 120 L630 0 Z" fill="url(#swoosh-back)"/>
      <path d="M495 0 C570 14 610 50 624 105" fill="none" stroke="#a6dc80" stroke-width="1.2" opacity="0.7"/>
    </svg>

    <p class="card-web">www.ifenlymedia-example.com</p>
  </section>

  <div class="side-label side-label--back">Bizcard Back</div>
</body>
</html>
```